Website incl. html for real estate project

We need the design and implementation of a website for a real estate project. Condominiums are built, which are sold.
We upload the sales brochure. The website should be based on the design of the sales brochure.
There are three houses with 5 apartments each. It should be rendered like this. The structure of the menu should be roughly as follows. Most information about the content is either in the appendix as a picture or in the brochure (PDF)):
Home (page 4-5 from the brochure)
House A
house B
house c
overview
basement
Municipal elections (page 6-7 in the brochure pdf)
Contact
Please use Roboto Regular as font.
And one page should give an overview of all apartments with the prices, the living space, etc. as on the file overview2.jpg.
If you go to the House A, House B, or House C menus, a page should come up with the details for that house only. The pages in the brochure are:
House A (Page 10-11)
House B (page 22-23)
House C (page 34-35)
The individual apartments should each be shown on a property page. There the plan / floor plan of the apartment and the pictures from the inside should be shown. As with the object page.jpg attachment.
Für die Designer... Mehr Zeit...
Coded - Design and coding required
1 page

```html
<!DOCTYPE html>
<html lang="de">
<head>
<meta charset="utf-8">
<title>Wohnpark am Lindenhof</title>
<link rel="stylesheet" href="https://fonts.googleapis.com/css2?family=Roboto:wght@300;400;500;700&display=swap">
<style>
:root{
  --blue:#115a8c;
  --blue-dark:#0d4b77;
  --red:#e1001a;
  --text:#4a4a4a;
  --heading:#1e1e1e;
  --line:#dedede;
  --footer:#1f2428;
  --white:#fff;
}
*{box-sizing:border-box;margin:0;padding:0}
html,body{width:1200px;height:4967px;overflow:hidden}
body{position:relative;font-family:'Roboto',sans-serif;color:var(--text);background:var(--white)}
h1,h2{font-weight:400}
.abs{position:absolute}
p{font-size:13.5px;line-height:24px;text-align:justify}
.btn{display:inline-flex;align-items:center;gap:10px;background:var(--red);color:#fff;font-weight:700;font-size:13px;text-transform:uppercase;padding:0 24px;height:44px;letter-spacing:.3px}
.btn .dot{width:14px;height:14px;border-radius:50%;background:#fff;display:inline-block;position:relative}
.btn .dot:after{content:"";position:absolute;left:4px;top:4px;border-left:6px solid var(--red);border-top:3px solid transparent;border-bottom:3px solid transparent}
.rule{width:42px;height:2px;background:var(--red);margin:14px 0 22px}

/* header */
.site-header{top:0;left:0;width:1200px;height:79px;background:#fff;box-shadow:0 1px 4px rgba(0,0,0,.08);z-index:5}
.brand{left:110px;top:24px;display:flex;align-items:center;gap:10px;font-weight:700;font-size:26px;color:var(--blue);letter-spacing:1px}
.brand .mark{width:14px;height:14px;background:var(--red)}
.nav{left:334px;top:34px;display:flex;gap:17px;font-size:13px;font-weight:500;color:#222}
.nav .active{color:var(--red)}
.callout{left:884px;top:22px;display:flex;gap:14px;align-items:center}
.callout .ring{width:36px;height:36px;border-radius:50%;background:var(--blue);display:flex;align-items:center;justify-content:center}
.callout small{display:block;font-size:11px;font-weight:700;color:#222}
.callout strong{font-size:19px;color:var(--red);font-weight:700}

/* hero */
.hero{top:79px;left:0;width:1200px;height:560px;overflow:hidden}
.hero-photo{position:absolute;inset:0;background:linear-gradient(180deg,#c9d3da 0%,#aab4b6 45%,#7c8c6c 70%,#4f7a3a 100%)}
.hero-label{color:#222;font-size:15px;font-weight:700}
.hero-title{left:600px;top:219px;color:#fff;font-size:76px;font-weight:400;line-height:74px}
.hero-sub{left:600px;top:390px;color:#fff;font-size:20px;font-weight:700}
.hero .btn{left:600px;top:436px;position:absolute}

/* about */
.about-title{left:110px;top:805px;font-size:29px;font-weight:400;color:var(--heading)}
.about-text{left:110px;top:872px;width:424px}
.about .btn{position:absolute;left:110px;top:1134px}
.about-photo{left:600px;top:760px;width:488px;height:554px;background:linear-gradient(160deg,#eaeaea,#bdbdbd 60%,#8f8f8f)}
.stats{left:110px;top:1239px;width:733px;height:172px;background:#fff;box-shadow:0 2px 10px rgba(0,0,0,.15);display:flex;padding:18px 0}
.stat{flex:1;text-align:center;border-right:1px solid var(--line);display:flex;flex-direction:column;align-items:center}
.stat:last-child{border-right:0}
.stat span{font-size:13.5px;color:#555;line-height:19px;margin-top:8px}
.stat b{font-size:40px;color:var(--blue);font-weight:700;line-height:44px}
.arrow-btn{width:28px;height:28px;border-radius:50%;background:#fff;box-shadow:0 1px 4px rgba(0,0,0,.25);display:flex;align-items:center;justify-content:center;top:1310px}

/* overview */
.overview{top:1507px;left:0;width:1200px;height:519px}
.plan{left:0;top:60px;width:618px;height:363px;background:linear-gradient(120deg,#d6d6d6,#b9a58d 60%,#9a8c7a)}
.overview-title{left:708px;top:1578px;font-size:29px;color:#fff;font-weight:400}
.overview-text{left:708px;top:1622px;width:420px;color:#fff}

/* houses */
.section-title{left:0;width:1200px;text-align:center;font-size:29px;font-weight:400;color:var(--heading);top:2108px}
.house-title{left:0;width:1200px;text-align:center;font-size:20px;font-weight:700;color:var(--heading)}
.house-text{left:110px;width:978px;text-align:center;font-size:13.5px;line-height:24px}
.unit-table{border-collapse:collapse;box-shadow:0 2px 10px rgba(0,0,0,.18);background:#fff;font-size:12px;color:#555;text-align:center;width:496px}
.unit-table td{border:1px solid var(--line);height:57px;line-height:16px;width:25%;padding:0 4px}

/* contact */
.contact{top:4055px;left:0;width:1200px;height:529px;background:var(--blue)}
.contact-title{left:110px;top:4124px;color:#fff;font-size:29px;font-weight:400}
.field{background:#fff;height:42px;font-size:12px;color:#666;padding:0 14px;display:flex;align-items:center;justify-content:space-between}

/* footer */
.footer{top:4584px;left:0;width:1200px;height:383px;background:var(--footer);color:#d9d9d9}
.foot-head{font-size:13px;font-weight:700;color:#fff;text-decoration:underline;text-transform:uppercase}
.foot-list{list-style:none;font-size:13.5px;line-height:34px}
.foot-list li:before{content:"»";margin-right:12px}
.contact-line{display:flex;gap:24px;align-items:center;font-size:13.5px;line-height:20px}
.contact-line i{width:28px;height:28px;border-radius:50%;border:1px solid #777;flex:none;display:flex;align-items:center;justify-content:center}
.social{width:30px;height:30px;border-radius:50%;border:1px solid #bbb}
.copyright{left:0;width:1200px;text-align:center;top:4940px;font-size:13px;color:#d9d9d9}
.foot-rule{left:110px;top:4900px;width:978px;height:1px;background:#444}
</style>
</head>
<body>

<header class="site-header abs">
  <div class="brand abs"><span class="mark"></span>BRUNNWALD</div>
  <nav class="nav abs">
    <span class="active">Heim</span><span>Haus A</span><span>Haus B</span><span>Haus c</span><span>Untergeschoss</span><span>Gemeindewahlen</span><span>Kontakt</span>
  </nav>
  <div class="callout abs">
    <div class="ring"><svg width="16" height="16" viewBox="0 0 24 24"><path fill="#fff" d="M6.6 10.8a15 15 0 0 0 6.6 6.6l2.2-2.2c.3-.3.7-.4 1-.2 1.1.4 2.3.6 3.6.6.6 0 1 .4 1 1V20c0 .6-.4 1-1 1A17 17 0 0 1 3 4c0-.6.4-1 1-1h3.5c.6 0 1 .4 1 1 0 1.3.2 2.5.6 3.6.1.3 0 .7-.2 1z"/></svg></div>
    <div><small>RUFEN SIE UNS AN !</small><strong>+41 61 555 20 40</strong></div>
  </div>
</header>

<section class="hero abs">
  <div class="hero-photo" role="img" aria-label="Aussenansicht der drei Mehrfamilienhäuser mit Rasen und Bäumen"></div>
  <svg class="abs" style="left:0;top:0" width="1200" height="560" viewBox="0 0 1200 560">
    <polygon points="523,560 523,320 950,40 1200,210 1200,560" fill="rgba(17,90,140,.82)"/>
    <polyline points="505,400 505,310 950,18 1200,185" fill="none" stroke="var(--red)" stroke-width="22"/>
    <polyline points="1200,250 1190,250 1190,560" fill="none" stroke="var(--red)" stroke-width="22"/>
    <polyline points="1030,530 1200,530" fill="none" stroke="var(--red)" stroke-width="22"/>
  </svg>
  <div class="hero-label abs" style="left:210px;top:126px">Haus C</div>
  <div class="hero-label abs" style="left:1128px;top:160px">Haus A</div>
  <div class="hero-label abs" style="left:641px;top:186px;color:#6c8cb0;font-weight:400">Haus B</div>
  <h1 class="hero-title abs">Wohnpark am<br>Lindenhof</h1>
  <div class="hero-sub abs">Hochwertige und moderne Eigentumswohnungen</div>
  <a class="btn">Loslegen <span class="dot"></span></a>
</section>

<section class="about">
  <h2 class="about-title abs">Wohnpark am Lindenhof</h2>
  <div class="about-text abs">
    <p>Die Überbauung mit drei Mehrfamilienhäusern und insgesamt 15 Eigentumswohnungen entsteht zwischen der Birkenstrasse und dem Mattenweg in Rainach im Tal. Die modernen und hochwertigen Wohnungen sind gegen das ruhige Quartier Mattenfeld und den wunderschönen Ausblick auf den grünen Hohbergkopf ausgerichtet.</p>
    <p>Die Wohnungen befinden sich an idealer Lage in Rainach mit guter Besonnung und die nächste Bushaltestelle ist nur knapp 120 Meter entfernt. Die Wohnungen sind im Obergeschoss mit grosszügigem</p>
  </div>
  <a class="btn">Lern mehr <span class="dot"></span></a>
  <div class="about-photo abs" role="img" aria-label="Helle Küche mit Esstisch und Hängeleuchten"></div>
  <div class="stats abs">
    <div class="stat"><svg width="64" height="60" viewBox="0 0 64 60"><polygon points="32,4 60,28 60,56 4,56 4,28" fill="var(--red)"/><polygon points="32,16 50,31 50,50 14,50 14,31" fill="var(--blue)"/><rect x="27" y="36" width="10" height="14" fill="#fff"/></svg><span>Gebäude mit individuellen<br>Wohnangebot</span><b>3</b></div>
    <div class="stat"><svg width="64" height="60" viewBox="0 0 64 60"><polygon points="32,4 60,28 60,56 4,56 4,28" fill="var(--red)"/><polygon points="32,16 50,31 50,50 14,50 14,31" fill="var(--blue)"/><rect x="27" y="36" width="10" height="14" fill="#fff"/></svg><span>unterschiedliche<br>Grundrisstypen</span><b>9</b></div>
    <div class="stat"><svg width="64" height="60" viewBox="0 0 64 60"><polygon points="32,4 60,28 60,56 4,56 4,28" fill="var(--red)"/><polygon points="32,16 50,31 50,50 14,50 14,31" fill="var(--blue)"/><rect x="27" y="36" width="10" height="14" fill="#fff"/></svg><span>Parkplätze in der<br>Tiefgarage</span><b>27</b></div>
  </div>
  <div class="arrow-btn abs" style="left:98px"><svg width="10" height="10" viewBox="0 0 10 10"><polyline points="7,1 3,5 7,9" fill="none" stroke="#333" stroke-width="1.6"/></svg></div>
  <div class="arrow-btn abs" style="left:826px"><svg width="10" height="10" viewBox="0 0 10 10"><polyline points="3,1 7,5 3,9" fill="none" stroke="#333" stroke-width="1.6"/></svg></div>
</section>

<section class="overview abs">
  <svg class="abs" style="left:0;top:0" width="1200" height="519" viewBox="0 0 1200 519">
    <polygon points="365,0 1200,0 1200,519 400,519 470,420 650,150" fill="var(--blue)"/>
    <polyline points="345,-10 665,160" fill="none" stroke="var(--red)" stroke-width="24"/>
    <polyline points="10,330 10,505 450,440" fill="none" stroke="var(--red)" stroke-width="24"/>
  </svg>
  <div class="plan abs" role="img" aria-label="Grundriss einer Wohnung mit möbliertem Wohn- und Essbereich"></div>
</section>
<h2 class="overview-title abs">Übersichtsplan</h2>
<div class="overview-text abs">
  <div class="rule" style="background:#fff"></div>
  <p>Die Überbauung mit drei Mehrfamilienhäusern und insgesamt 15 Eigentumswohnungen entsteht zwischen der Birkenstrasse und dem Mattenweg in Rainach im Tal. Die modernen und hochwertigen Wohnungen sind gegen das ruhige Quartier Mattenfeld und den wunderschönen Ausblick auf den grünen Hohbergkopf ausgerichtet.</p>
  <p>Die Wohnungen befinden sich an idealer Lage in Rainach mit guter Besonnung und die nächste Bushaltestelle ist nur knapp 120 Meter entfernt. Die Wohnungen sind im Obergeschoss mit grosszügigem</p>
</div>
<a class="btn abs" style="left:708px;top:1905px">Lern mehr <span class="dot"></span></a>

<h2 class="section-title abs">Die Hauser</h2>

<!-- Haus A -->
<h3 class="house-title abs" style="top:2190px">Wohnpark am Lindenhof Haus A</h3>
<div class="house-text abs" style="top:2230px">Das Gebäude «Haus A» verfügt über fünf moderne Wohnungen mit individuellen Grundrissen. Alle Wohnungen haben einen grosszügigen Aussenbereich mit Balkon oder gedecktem Sitzplatz in Richtung Süden zum Hohbergkopf, dem Rainacher Hausberg, ausgerichtet. Die Wohnräume sind mit grossen Fenstern ausgestattet, was die Räume mit Sonnenlicht durchflutet. Das Gebäude ist direkt aus der Tiefgarage mit dem Lift zugänglich</div>
<svg class="abs" style="left:108px;top:2334px" width="402" height="380" viewBox="0 0 402 380" role="img" aria-label="Helles Wohnzimmer mit Esstheke und Wandbild">
  <defs><linearGradient id="gA" x1="0" y1="0" x2="1" y2="1"><stop offset="0" stop-color="#f1f1f1"/><stop offset=".6" stop-color="#cfcbc6"/><stop offset="1" stop-color="#8d857c"/></linearGradient></defs>
  <polygon points="0,140 180,0 402,120 402,280 380,280 380,120 180,24 22,150 22,200 0,200" fill="var(--red)"/>
  <polygon points="8,380 8,210 30,210 30,160 180,42 370,134 370,380" fill="url(#gA)"/>
</svg>
<table class="unit-table abs" style="left:592px;top:2382px">
  <tr><td>Attika Wohnung</td><td>4.5 Zimmer</td><td>108 m2<br>Wohnfl äche</td><td>105 m2 grosse<br>Sonnenterrasse !</td></tr>
  <tr><td>Obergeschoss</td><td>3.5 Zimmer</td><td>81 m2<br>Wohnfl äche</td><td>16 m2<br>grosser Balkon</td></tr>
  <tr><td>Obergeschoss</td><td>4.5 Zimmer</td><td>102 m2<br>Wohnfl äche</td><td>33 m2<br>grosser Balkon</td></tr>
  <tr><td>Erdgeschoss</td><td>3.5 Zimmer</td><td>81 m2<br>Wohnfl äche</td><td>16 m2<br>gedeckter Sitzplatz</td></tr>
  <tr><td>Erdgeschoss</td><td>4.5 Zimmer</td><td>102 m2<br>Wohnfl äche</td><td>33 m2<br>gedeckter Sitzplatz</td></tr>
</table>

<!-- Haus B -->
<h3 class="house-title abs" style="top:2800px">Wohnpark am Lindenhof Haus B</h3>
<div class="house-text abs" style="top:2840px">Das Gebäude «Haus B» verfügt über fünf moderne Wohnungen mit individuellen Grundrissen. Alle Wohnungen haben einen grosszügigen Balkon oder Terrasse Richtung Süden zum Hohbergkopf, dem Rainacher Hausberg, ausgerichtet. Die Wohnräume sind mit grossen Fenstern ausgestattet was die Räume mit hellem Sonnenlicht</div>
<table class="unit-table abs" style="left:112px;top:2972px">
  <tr><td>Attika Wohnung</td><td>4.5 Zimmer</td><td>109 m2<br>Wohnfl äche</td><td>107 m2 grosse<br>Sonnenterrasse !</td></tr>
  <tr><td>Obergeschoss</td><td>2.5 Zimmer</td><td>69 m2<br>Wohnfl äche</td><td>14 m2<br>grosse Balkon</td></tr>
  <tr><td>Obergeschoss</td><td>2.5 Zimmer</td><td>117 m2<br>Wohnfl äche</td><td>42 m2<br>grosse Balkon</td></tr>
  <tr><td>Erdgeschoss</td><td>4.5 Zimmer</td><td>117 m2<br>Wohnfl äche</td><td>14 m2<br>gedeckter Sitzplatz</td></tr>
  <tr><td>Untergeschoss</td><td>Hobbyraum</td><td>24 m2<br>Flächen</td><td>42 m2<br>gedeckter Sitzplatz</td></tr>
</table>
<svg class="abs" style="left:688px;top:2942px" width="402" height="380" viewBox="0 0 402 380" role="img" aria-label="Wohnzimmer mit Sofa und grossen Fenstern">
  <defs><linearGradient id="gB" x1="0" y1="0" x2="1" y2="1"><stop offset="0" stop-color="#f4f2ef"/><stop offset=".6" stop-color="#d8d1c6"/><stop offset="1" stop-color="#a59a8a"/></linearGradient></defs>
  <polygon points="0,120 222,0 402,140 402,200 380,200 380,150 222,24 22,120 22,280 0,280" fill="var(--red)"/>
  <polygon points="32,380 32,134 222,42 372,160 372,210 394,210 394,380" fill="url(#gB)"/>
</svg>

<!-- Haus C -->
<h3 class="house-title abs" style="top:3408px">Wohnpark am Lindenhof Haus C</h3>
<div class="house-text abs" style="top:3448px">Das Gebäude «Haus C» verfügt über fünf moderne Wohnungen mit individuellen und gross ausgelegten Grundrissen. Alle Wohnungen haben einen grosszügigen Balkon oder Terrasse in Richtung Hohbergkopf, dem Rainacher Hausberg, ausgerichtet. Die Wohnräume sind mit grossen Fenstern ausgestattet, was die Räume mit Sonnenlicht durchflutet. Das Gebäude ist direkt aus der Tiefgarage mit dem Lift zugänglich</div>
<svg class="abs" style="left:108px;top:3550px" width="402" height="380" viewBox="0 0 402 380" role="img" aria-label="Offener Wohn- und Essbereich mit Fensterfront">
  <defs><linearGradient id="gC" x1="0" y1="0" x2="1" y2="1"><stop offset="0" stop-color="#ececec"/><stop offset=".55" stop-color="#bdb3a6"/><stop offset="1" stop-color="#6f655a"/></linearGradient></defs>
  <polygon points="0,140 180,0 402,120 402,280 380,280 380,120 180,24 22,150 22,200 0,200" fill="var(--red)"/>
  <polygon points="8,380 8,210 30,210 30,160 180,42 370,134 370,380" fill="url(#gC)"/>
</svg>
<table class="unit-table abs" style="left:592px;top:3601px">
  <tr><td>Attika Wohnung</td><td>4.5 Zimmer</td><td>129 m2<br>Wohnfl äche</td><td>132 m2 grosse<br>Sonnenterrasse !</td></tr>
  <tr><td>Obergeschoss</td><td>3.5 Zimmer</td><td>143 m2<br>Wohnfl äche</td><td>43 m2<br>grosser Balkon</td></tr>
  <tr><td>Erdgeschoss</td><td>5.5 Zimmer</td><td>143 m2<br>Wohnfl äche</td><td>23 m2<br>grosser Balkon</td></tr>
  <tr><td>Erdgeschoss</td><td>3.5 Zimmer</td><td>96 m2<br>Wohnfl äche</td><td>43 m2 gedeckter<br>Sitzplatz</td></tr>
  <tr><td>Untergeschoss</td><td>Hobbyraum</td><td>43 m2<br>Fläche</td><td>mit Dusche/Lavabo<br>und Toilette</td></tr>
</table>

<!-- contact -->
<section class="contact abs">
  <svg class="abs" style="left:580px;top:-10px" width="620" height="549" viewBox="0 0 620 549" role="img" aria-label="Stadtplan mit Standortmarkierung">
    <defs><linearGradient id="gM" x1="0" y1="0" x2="1" y2="1"><stop offset="0" stop-color="#eef1e6"/><stop offset=".5" stop-color="#dfe6ea"/><stop offset="1" stop-color="#a9cfe8"/></linearGradient></defs>
    <polygon points="0,110 250,0 620,40 620,549 120,549 0,470" fill="var(--red)"/>
    <polygon points="40,150 260,40 600,60 600,520 140,520 40,440" fill="url(#gM)"/>
    <path d="M377 250c-10 0-17 7-17 17 0 12 17 32 17 32s17-20 17-32c0-10-7-17-17-17z" fill="#b8860b"/>
    <circle cx="377" cy="267" r="6" fill="#fff"/>
  </svg>
  <div class="abs" style="left:110px;top:125px;width:42px;height:2px;background:#fff"></div>
</section>
<h2 class="contact-title abs">In Kontakt kommen</h2>
<div class="field abs" style="left:110px;top:4206px;width:200px">Vorname <svg width="11" height="11" viewBox="0 0 12 12"><circle cx="6" cy="3.5" r="3" fill="#555"/><path d="M0 12c0-4 3-5.5 6-5.5s6 1.5 6 5.5z" fill="#555"/></svg></div>
<div class="field abs" style="left:323px;top:4206px;width:200px">Nachname <svg width="11" height="11" viewBox="0 0 12 12"><circle cx="6" cy="3.5" r="3" fill="#555"/><path d="M0 12c0-4 3-5.5 6-5.5s6 1.5 6 5.5z" fill="#555"/></svg></div>
<div class="field abs" style="left:110px;top:4268px;width:200px">Telefon-Nr <svg width="11" height="11" viewBox="0 0 24 24"><path fill="#555" d="M6.6 10.8a15 15 0 0 0 6.6 6.6l2.2-2.2c.3-.3.7-.4 1-.2 1.1.4 2.3.6 3.6.6.6 0 1 .4 1 1V20c0 .6-.4 1-1 1A17 17 0 0 1 3 4c0-.6.4-1 1-1h3.5c.6 0 1 .4 1 1 0 1.3.2 2.5.6 3.6.1.3 0 .7-.2 1z"/></svg></div>
<div class="field abs" style="left:323px;top:4268px;width:200px">Dienstleistungen <svg width="9" height="6" viewBox="0 0 9 6"><polygon points="0,0 9,0 4.5,6" fill="#555"/></svg></div>
<div class="field abs" style="left:110px;top:4328px;width:413px;height:94px;align-items:flex-start;padding-top:14px">Zusätzliche Kommentare oder Einstellungen <svg width="12" height="11" viewBox="0 0 12 11"><ellipse cx="6" cy="5" rx="5.3" ry="4" fill="none" stroke="#555"/></svg></div>
<a class="btn abs" style="left:110px;top:4455px;height:42px">Jetzt absenden <span class="dot"></span></a>

<!-- footer -->
<footer class="footer abs">
  <div class="foot-head abs" style="left:110px;top:68px">Kontaktiere uns</div>
  <div class="contact-line abs" style="left:110px;top:108px"><i><svg width="10" height="13" viewBox="0 0 10 13"><path d="M5 0a5 5 0 0 0-5 5c0 4 5 8 5 8s5-4 5-8a5 5 0 0 0-5-5z" fill="#ddd"/><circle cx="5" cy="5" r="1.8" fill="#1f2428"/></svg></i><span>12 , Brunnwald Immobilien<br>AG Schweiz</span></div>
  <div class="contact-line abs" style="left:110px;top:172px"><i><svg width="12" height="9" viewBox="0 0 12 9"><rect x=".5" y=".5" width="11" height="8" fill="none" stroke="#ddd"/><polyline points=".5,.5 6,5 11.5,.5" fill="none" stroke="#ddd"/></svg></i><span>info@brunnwald-immo.ch</span></div>
  <div class="contact-line abs" style="left:110px;top:232px"><i><svg width="12" height="12" viewBox="0 0 24 24"><path fill="#ddd" d="M6.6 10.8a15 15 0 0 0 6.6 6.6l2.2-2.2c.3-.3.7-.4 1-.2 1.1.4 2.3.6 3.6.6.6 0 1 .4 1 1V20c0 .6-.4 1-1 1A17 17 0 0 1 3 4c0-.6.4-1 1-1h3.5c.6 0 1 .4 1 1 0 1.3.2 2.5.6 3.6.1.3 0 .7-.2 1z"/></svg></i><span style="font-size:18px;color:#fff;font-weight:500">+41 61 555 20 40</span></div>

  <div class="foot-head abs" style="left:432px;top:68px">Schnelle Links</div>
  <ul class="foot-list abs" style="left:432px;top:98px">
    <li>Heim</li><li>Über uns</li><li>Unsere Leistungen</li><li>Warum uns wählen</li><li>Bewertungen</li>
  </ul>
  <div class="foot-head abs" style="left:670px;top:68px">Andere Verbindungen</div>
  <ul class="foot-list abs" style="left:670px;top:98px">
    <li>Kontaktiere uns</li><li>FAQ</li><li>Hilfsdienst</li><li>Nutzungsbedingungen</li><li>Datenschutz-Bestimmungen</li>
  </ul>
  <div class="abs" style="left:908px;top:120px;display:flex;align-items:center;gap:10px;font-size:24px;font-weight:700;color:#fff;letter-spacing:1px"><span style="width:12px;height:12px;background:#fff;display:inline-block"></span>BRUNNWALD</div>
  <div class="abs" style="left:920px;top:182px;display:flex;gap:10px">
    <span class="social"></span><span class="social"></span><span class="social"></span><span class="social"></span>
  </div>
</footer>
<div class="foot-rule abs"></div>
<div class="copyright abs">© 2022 Brunnwald. Alle Rechte vorbehalten</div>

</body>
</html>
```